Up to the Challenge? Canadian based consulting company needs a two sided business card design

A Canadian based security risk management consulting company needs a two-sided business card design. What we do is provide advice and guidance related to emergency, security and business continuity management for small, medium and large companies to help ensure the protection of their people, assets, information, services, operations and reputation.

The final design should be simple, only one or two colours, eye catching, professional and one that makes people look at three or more times just because it looks so darn good.

I have include examples of business cards I like.

Target Market(s)

Small, medium and large companies.

Industry/Entity Type

Security

Contact Information for Business Card

Business Card Size: Standard size of 3.5" (89mm) x 2.0" (51mm) - (see full specifications and guides on PRINTA's website if required)
Card Stock: Looking to use PRINTA's Velda 32pt stock textured paper - seam colour either chili red or black
Business Name: The Harrowfield Group
Website: www.theharrowfieldgroup.example
Telephone: (555)214-0397
Name: Dana Forsythe
Position: Principle
e-mail: Dana.Forsythe@theharrowfieldgroup.example

Font styles to use
Serif

Colors
ec1f27
000000
9d9d9d
aaaaaa
606060

Requirements
Must have
• - "The Harrowfield Group" logo (see uploaded files). I have included grey scale and colour versions.
• - Business card details (as above)
Nice to have
• - One side black or grey scale.
• - Other side would likely be white.
• - Everyone likes the silver logo on the black background.
• - Small element of colour i.e. red but I'm leaning more to greyscale.
Should not have
• - A lot of colour. Keep it simple.

```html
<!DOCTYPE html>
<html lang="en">
<head>
<meta charset="utf-8">
<title>The Harrowfield Group – Business Card</title>
<link rel="stylesheet" href="https://fonts.googleapis.com/css2?family=Noto+Serif:wght@400;500&display=swap">
<style>
  :root {
    --page: #e9eaea;
    --card-white: #ffffff;
    --card-edge: #c9cccc;
    --stone: #95a3a1;
    --ink: #3a3a3a;
    --ink-soft: #444444;
    --mark: #505050;
    --on-stone: #ffffff;
  }
  html, body {
    margin: 0;
    padding: 0;
    width: 1200px;
    height: 1200px;
    overflow: hidden;
    background: var(--page);
    font-family: "Noto Serif", Georgia, serif;
  }
  .canvas {
    position: relative;
    width: 1200px;
    height: 1200px;
  }
  .card {
    position: absolute;
    width: 840px;
    height: 480px;
    overflow: hidden;
    box-sizing: border-box;
    border: 1px solid var(--card-edge);
  }
  .card-back {
    left: 329px;
    top: 631px;
    background: var(--stone);
  }
  .card-back .corner {
    position: absolute;
    left: 0;
    top: 0;
    width: 229px;
    height: 229px;
    background: var(--card-white);
    clip-path: polygon(0 0, 100% 0, 0 100%);
  }
  .card-front {
    left: 76px;
    top: 214px;
    background: var(--card-white);
  }
  .card-front .corner {
    position: absolute;
    right: 0;
    top: 0;
    width: 230px;
    height: 230px;
    background: var(--stone);
    clip-path: polygon(0 0, 100% 0, 100% 100%);
  }
  .brand-square {
    position: absolute;
    left: 164px;
    top: 222px;
    width: 84px;
    height: 84px;
    background: var(--mark);
  }
  .brand-name,
  .brand-sub,
  .website {
    position: absolute;
    left: 0;
    width: 412px;
    margin: 0;
    text-align: center;
    line-height: 1;
    color: var(--ink);
  }
  .brand-name {
    top: 342px;
    font-weight: 500;
    font-size: 33px;
    letter-spacing: 0.01em;
  }
  .brand-sub {
    top: 378px;
    font-weight: 500;
    font-size: 21px;
    letter-spacing: 0.22em;
  }
  .website {
    top: 421px;
    font-size: 21px;
    color: var(--ink-soft);
  }
  .contact {
    position: absolute;
    right: 41px;
    top: 258px;
    text-align: right;
    color: var(--on-stone);
  }
  .person-name {
    margin: 0;
    font-size: 45px;
    font-weight: 400;
    line-height: 1.05;
  }
  .person-role {
    margin: 2px 0 0;
    font-size: 32px;
    line-height: 1.1;
  }
  .details {
    margin: 38px 0 0;
    font-size: 23px;
    line-height: 1.36;
  }
</style>
</head>
<body>
  <main class="canvas">
    <section class="card card-back" aria-label="Card back">
      <div class="corner"></div>
      <div class="contact">
        <h1 class="person-name">DANA FORSYTHE</h1>
        <p class="person-role">PRINCIPLE</p>
        <p class="details">(555)214-0397<br>Dana.Forsythe@theharrowfieldgroup.example</p>
      </div>
    </section>

    <section class="card card-front" aria-label="Card front">
      <div class="corner"></div>
      <span class="brand-square" aria-hidden="true"></span>
      <p class="brand-name">THE HARROWFIELD</p>
      <p class="brand-sub">GROUP</p>
      <p class="website">www.theharrowfieldgroup.example</p>
    </section>
  </main>
</body>
</html>
```